Financial Advisor needs a BOLD Business Card

I need a business card that is professional, and is also eye-catching and memorable. I would like to include my photo (several different professional photos have been uploaded). Preferred primary color is blue, or green, or dark purple. The final design should have a modern/contemporary look while communicating a professional image.

Target Market(s)

Individual Investors and Small Business Owners

Industry/Entity Type

Business

Contact Information for Business Card

[side 1:] Dale Korvanek Financial Advisor 58271 Marbleton Creek Rd., #340 St. Louis, MO 63907 (314) 555-0182 main (314) 555-0927 cell (314) 555-0346 fax daleK@qrvlx.com [side 2:] Life Insurance | Retirement | Employee Benefits

Font styles to use
Serif
Sans Serif

Requirements
Must have
• [disclaimer, text can be 7-9 point:] Securities offered through the B.W. Harbor Trading Company. Member NARCU/TLOB. Four Quarry Plaza, Cincinnati, Ohio 45917. 513-555-0263. Investment Advisory Services offered through B.W. Holdings Management Company.
Nice to have
• Bright, Light & Airy feel on Side 1 with contact data, bold patterns, high color contrast, modern or 3D look
Should not have
• Any symbols referring to money (e.g. $)

```html
<!DOCTYPE html>
<html lang="en">
<head>
<meta charset="utf-8">
<title>Dale Korvanek – Financial Advisor Business Card</title>
<link rel="stylesheet" href="https://fonts.googleapis.com/css2?family=Mulish:wght@300;400;700;800&display=swap">
<style>
  :root {
    --teal: #1fb2cc;
    --teal-deep: #169fb8;
    --white: #ffffff;
    --ink: #2b2b2b;
    --ink-soft: #555555;
    --icon-blue: #2aa6d6;
    --icon-purple: #6a3d8f;
    --page: #e9ebed;
  }
  * { box-sizing: border-box; margin: 0; padding: 0; }
  html, body { width: 1200px; height: 873px; overflow: hidden; }
  body {
    background: var(--page);
    font-family: "Mulish", "Century Gothic", sans-serif;
    position: relative;
  }
  .card {
    position: absolute;
    top: 286px;
    width: 525px;
    height: 300px;
    background: var(--teal);
    overflow: hidden;
    box-shadow: 0 6px 18px rgba(0,0,0,0.18);
  }
  .card--front { left: 50px; }
  .card--back { left: 625px; }

  /* Front */
  .contact-band {
    position: absolute;
    left: 0; right: 0;
    top: 42px;
    height: 166px;
    background: var(--white);
  }
  .portrait {
    position: absolute;
    left: 168px;
    top: 6px;
    width: 84px;
    height: 84px;
    border-radius: 50%;
    border: 3px solid var(--teal-deep);
    background: radial-gradient(circle at 50% 40%, #c9a07a 0%, #8a6a52 35%, #3c4a63 70%, #2c3140 100%);
  }
  .identity {
    position: absolute;
    left: 18px;
    top: 56px;
  }
  .identity__name {
    font-size: 17px;
    color: var(--ink);
    font-weight: 300;
    letter-spacing: 0.2px;
  }
  .identity__name strong { font-weight: 800; }
  .identity__title {
    font-size: 12px;
    font-weight: 400;
    color: var(--ink-soft);
    margin-top: 1px;
  }
  .contact-list {
    position: absolute;
    right: 18px;
    top: 100px;
    list-style: none;
    text-align: right;
  }
  .contact-list li {
    display: flex;
    justify-content: flex-end;
    align-items: center;
    gap: 7px;
    font-size: 12px;
    line-height: 17px;
    color: var(--ink);
  }
  .contact-list li.address { align-items: flex-start; }
  .contact-list svg { width: 10px; height: 10px; flex: none; }
  .contact-list li.address svg { margin-top: 4px; }
  .disclaimer {
    position: absolute;
    left: 18px;
    right: 24px;
    top: 222px;
    font-size: 9.5px;
    line-height: 13px;
    font-weight: 300;
    color: var(--white);
  }

  /* Back */
  .services {
    position: absolute;
    left: 34px;
    top: 34px;
    font-size: 13px;
    font-weight: 700;
    color: var(--white);
    letter-spacing: 0.6px;
    word-spacing: 2px;
  }
</style>
</head>
<body>
  <section class="card card--front" aria-label="Business card front">
    <div class="contact-band"></div>
    <div class="portrait" role="img" aria-label="Portrait photo of Dale Korvanek"></div>
    <div class="identity">
      <p class="identity__name">Dale <strong>Korvanek</strong></p>
      <p class="identity__title">Financial Advisor</p>
    </div>
    <ul class="contact-list">
      <li>(314) 555-0182
        <svg viewBox="0 0 10 10" aria-hidden="true"><path d="M2 1 L4 1 L4.6 3 L3.4 3.8 Q4.4 5.8 6.2 6.6 L7 5.4 L9 6 L9 8 Q9 9 8 9 Q1 8.4 1 2 Q1 1 2 1 Z" fill="var(--icon-blue)"/></svg>
      </li>
      <li>(314) 555-0927
        <svg viewBox="0 0 10 10" aria-hidden="true"><rect x="2.5" y="0.5" width="5" height="9" rx="1" fill="none" stroke="var(--icon-blue)" stroke-width="1.2"/><circle cx="5" cy="8" r="0.6" fill="var(--icon-blue)"/></svg>
      </li>
      <li>(314) 555-0346
        <svg viewBox="0 0 10 10" aria-hidden="true"><rect x="1" y="3" width="8" height="6" rx="0.8" fill="var(--icon-blue)"/><rect x="3" y="0.8" width="4" height="3" fill="none" stroke="var(--icon-blue)" stroke-width="1"/></svg>
      </li>
      <li>daleK@qrvlx.com
        <svg viewBox="0 0 10 10" aria-hidden="true"><rect x="0.8" y="2" width="8.4" height="6" fill="none" stroke="var(--icon-blue)" stroke-width="1.1"/><path d="M0.8 2 L5 5.5 L9.2 2" fill="none" stroke="var(--icon-blue)" stroke-width="1.1"/></svg>
      </li>
      <li class="address">58271 Marbleton Creek Rd., #340 St.<br>Louis, MO 63907
        <svg viewBox="0 0 10 10" aria-hidden="true"><path d="M5 9.5 Q1.5 5.5 1.5 3.6 A3.5 3.5 0 0 1 8.5 3.6 Q8.5 5.5 5 9.5 Z" fill="var(--icon-purple)"/><circle cx="5" cy="3.6" r="1.2" fill="var(--white)"/></svg>
      </li>
    </ul>
    <p class="disclaimer">Securities offered through the B.W. Harbor Trading Company. Member NARCU/TLOB. Four Quarry Plaza, Cincinnati, Ohio 45917. 513-555-0263. Investment Advisory Services offered through B.W. Holdings Management Company.</p>
  </section>

  <section class="card card--back" aria-label="Business card back">
    <p class="services">Life Insurance | Retirement | Employee Benefits</p>
  </section>
</body>
</html>
```